Kelvora Template

Hi Guys,

I have just completed a logo design with Vantelo Works and I am very happy with what I have seen so far. Next I would like to create a template for the site that will be skinned into a DNN skin.

Our goal with Kelvora is to create a site were people can register and buy a e-commerce site from us. The site needs to match the logo color scheme and entice people to register. The site needs to be clear on what they are receiving and make sure that the registration process is easily accessible. our target market is the Joe Soup's that want to create an online presence and sell their products.

I'm excited to see what you guys are going to come up with.

Regards

Willem

Hi all,

Thank you for your inputs, It was hard to choose a template as I feel that so many of them where so good.

Well done.

Regards

Willem Badenhorst

```html
<!DOCTYPE html>
<html lang="en">
<head>
<meta charset="utf-8">
<title>Kelvora</title>
<link rel="stylesheet" href="https://fonts.googleapis.com/css2?family=Cabin:wght@400;500;600&family=Oranienbaum&display=swap">
<style>
:root{
  --navy:#1f3a6b;
  --orange:#e8500a;
  --orange-text:#ff6a1a;
  --accent:#f07a1e;
  --ink:#1a1a1a;
  --heading:#1f3a6b;
  --teal:#1faec4;
  --teal-dark:#1a7fa8;
  --blue-btn:#2f6fc7;
  --line:#d8d8d8;
  --white:#fff;
}
*{box-sizing:border-box;margin:0;padding:0}
html,body{width:960px;height:1200px;overflow:hidden;background:var(--white);font-family:"Cabin",sans-serif;color:var(--ink)}
.page{position:relative;width:960px;height:1200px}
.abs{position:absolute}
.topbar{left:0;top:0;width:960px;height:33px;background:var(--navy)}
.home-btn{left:19px;top:6px;width:31px;height:27px;background:var(--white);border-radius:4px 4px 0 0;display:flex;align-items:center;justify-content:center}
.util-links{right:10px;top:0;height:33px;display:flex;gap:22px;align-items:center;color:var(--white);font-size:13px}
.util-links span{display:flex;align-items:center;gap:6px}
.brand{left:30px;top:68px;display:flex;align-items:center;gap:10px}
.brand-mark{width:34px;height:34px;background:var(--accent);border-radius:4px}
.brand-name{font-size:42px;font-weight:600;color:var(--navy);letter-spacing:-.5px;line-height:1}
.welcome{left:476px;top:73px;font-size:12px}
.welcome .hl{color:var(--accent)}
.account-links{left:442px;top:101px;font-size:11.5px;display:flex;gap:12px}
.cart-box{left:763px;top:63px;width:185px;height:58px;border:1px solid var(--line);border-radius:4px;display:flex;overflow:hidden;background:#fafafa}
.cart-icon{width:66px;background:var(--accent);display:flex;align-items:center;justify-content:center}
.cart-info{padding:8px 0 0 8px;font-size:13px}
.cart-info .sum{color:var(--accent);margin-top:4px}
.cart-info .sum b{color:var(--ink);font-weight:400}
.platforms{left:10px;top:151px;width:940px;height:48px;background:#000;display:flex;justify-content:space-around;align-items:center;padding:0 8px;font-size:12.5px;color:var(--orange-text)}
.search-band{left:10px;top:202px;width:940px;height:100px;background:var(--orange)}
.search-title{left:20px;top:209px;color:var(--white);font-size:18px}
.field{top:237px;height:27px;background:var(--white);border:1px solid #c9c9c9;font-size:11px;font-style:italic;color:#999;padding:6px 9px;display:flex;justify-content:space-between}
.palette{left:499px;top:264px}
.btn-dark{top:237px;height:25px;background:#1b1b1b;color:var(--white);font-size:11px;display:flex;align-items:center;justify-content:center;gap:14px}
.sidebar{left:13px;top:312px;width:180px;height:796px;border-right:1px solid var(--line)}
.sidebar h2{font-weight:500;font-size:15px;color:var(--heading);margin:2px 0 8px 1px}
.cat-list{list-style:none;font-size:12.5px}
.cat-list li{height:19.2px;padding-left:22px;position:relative}
.cat-list li::before{content:"";position:absolute;left:9px;top:6px;width:6px;height:5px;border-top:1.5px solid var(--accent);border-right:1.5px solid var(--accent);transform:rotate(45deg) skew(10deg);width:4px;height:4px}
.cat-list li.more{font-style:italic;padding-left:22px}
.cat-list li.more::before{display:none}
.hero{left:202px;top:313px;width:511px;height:210px;background:linear-gradient(160deg,#29bccb,var(--teal) 45%,var(--teal-dark));text-align:center;color:var(--white);font-family:"Oranienbaum",serif}
.hero h1{font-weight:400;font-size:46px;margin-top:30px;line-height:1}
.hero p{font-size:29px;color:#111;margin-top:14px}
.hero .cta{display:inline-block;margin-top:16px;width:206px;height:45px;border:2px solid #f3e1cf;border-radius:8px;background:linear-gradient(#f58a3c,#e65e10);font-size:24px;line-height:41px}
.featured-site{left:722px;top:313px;width:228px;height:210px;border:1px solid var(--line);text-align:center}
.featured-site h3{font-weight:400;font-size:19px;color:var(--teal-dark);margin-top:8px;padding-bottom:6px;border-bottom:1px solid #e5e5e5;margin-left:10px;margin-right:10px}
.site-shot{margin:8px auto 0;width:192px;height:152px;background:linear-gradient(90deg,#222,#6d6d6d 50%,#2b2b2b)}
.section-title{left:201px;top:548px;font-size:23px;font-weight:400;color:var(--heading)}
.pager{left:809px;top:565px;font-size:12px;color:var(--navy);display:flex;gap:5px;align-items:center}
.pager .cur{color:var(--accent)}
.pager i{width:13px;height:13px;border-radius:50%;background:#ddd;display:inline-block}
.tile{width:216px;text-align:center}
.thumb{height:166px;box-shadow:0 4px 5px -2px rgba(0,0,0,.35)}
.add-btn{display:inline-flex;align-items:center;gap:8px;margin-top:10px;height:32px;padding:0 14px 0 10px;border-radius:16px;background:linear-gradient(#5a95e0,var(--blue-btn));color:var(--white);font-size:11.5px}
.add-btn::before{content:"›";font-size:12px}
.tile-links{margin-top:9px;font-size:11.5px}
.footer{left:0;top:1120px;width:960px;height:80px;background:var(--navy);color:var(--white);font-size:11px;text-align:center}
.footer nav{padding-top:22px;word-spacing:2px}
.footer nav span{margin:0 9px}
.footer .copy{margin-top:14px}
</style>
</head>
<body>
<div class="page">
  <div class="abs topbar"></div>
  <div class="abs home-btn"><svg width="20" height="18" viewBox="0 0 20 18"><path d="M2 9 10 2l8 7" fill="none" stroke="#1f3a6b" stroke-width="2.4"/><path d="M5 9v8h10V9" fill="none" stroke="#1f3a6b" stroke-width="2.4"/></svg></div>
  <div class="abs util-links">
    <span><svg width="16" height="16"><circle cx="8" cy="8" r="7" fill="none" stroke="#fff" stroke-width="1.3"/><path d="M8 7v5M8 4v1.5" stroke="#fff" stroke-width="1.6"/></svg>About Us</span>
    <span><svg width="14" height="14"><rect x="5" y="1" width="4" height="3" fill="#fff"/><rect x="1" y="9" width="4" height="3" fill="#fff"/><rect x="9" y="9" width="4" height="3" fill="#fff"/><path d="M7 4v3M3 9V7h8v2" stroke="#fff" fill="none"/></svg>Site Map</span>
    <span><svg width="18" height="18"><circle cx="9" cy="9" r="8" fill="none" stroke="#fff" stroke-width="1.3"/><text x="9" y="13" text-anchor="middle" fill="#fff" font-size="11" font-family="Cabin,sans-serif">?</text></svg>Help &amp; Support</span>
  </div>

  <div class="abs brand"><div class="brand-mark"></div><div class="brand-name">Kelvora</div></div>
  <div class="abs welcome">Welcome <span class="hl">Guest,</span>&nbsp; you can &nbsp;<span class="hl">Login</span>&nbsp; or &nbsp;<span class="hl">Create an Account</span></div>
  <div class="abs account-links"><span>WISH LIST (0)</span><span>MY ACCOUNT</span><span>SHOPPING CART</span><span>CHECKOUT</span></div>
  <div class="abs cart-box">
    <div class="cart-icon"><svg width="34" height="30" viewBox="0 0 34 30"><path d="M2 3h5l4 17h17l3-12H9" fill="none" stroke="#fff" stroke-width="2.5"/><circle cx="13" cy="26" r="2.5" fill="#fff"/><circle cx="26" cy="26" r="2.5" fill="#fff"/></svg></div>
    <div class="cart-info"><div>SHOPPING CART</div><div class="sum">0 item(s) <b>- $0.00</b></div></div>
  </div>

  <nav class="abs platforms"><span>Calderon Themes</span><span>Brightshelf Themes</span><span>Verimart Templates</span><span>Quillshop Themes</span><span>Opalcommerce Templates</span><span>Stillcart Templates</span><span>Lanterncart Templates</span></nav>

  <div class="abs search-band"></div>
  <div class="abs search-title">Search</div>
  <div class="abs field" style="left:51px;width:197px"><span>Category</span><span>▽</span></div>
  <div class="abs field" style="left:262px;width:223px"><span>Keywords (If any..)</span></div>
  <div class="abs field" style="left:499px;width:184px"><span>Colors (If any..)</span><span>▽</span></div>
  <svg class="abs palette" width="184" height="47" viewBox="0 0 184 47">
    <rect width="184" height="47" fill="#333"/>
    <g stroke="#333" stroke-width=".8">
      <rect x="0" y="0" width="11.5" height="11.7" fill="#f00"/><rect x="11.5" y="0" width="11.5" height="11.7" fill="#ff0"/><rect x="23" y="0" width="11.5" height="11.7" fill="#0f0"/><rect x="34.5" y="0" width="11.5" height="11.7" fill="#0ff"/><rect x="46" y="0" width="11.5" height="11.7" fill="#00f"/><rect x="57.5" y="0" width="11.5" height="11.7" fill="#f0f"/><rect x="69" y="0" width="11.5" height="11.7" fill="#fff"/><rect x="80.5" y="0" width="11.5" height="11.7" fill="#eee"/><rect x="92" y="0" width="11.5" height="11.7" fill="#ddd"/><rect x="103.5" y="0" width="11.5" height="11.7" fill="#ccc"/><rect x="115" y="0" width="11.5" height="11.7" fill="#bbb"/><rect x="126.5" y="0" width="11.5" height="11.7" fill="#aaa"/><rect x="138" y="0" width="11.5" height="11.7" fill="#999"/><rect x="149.5" y="0" width="11.5" height="11.7" fill="#888"/><rect x="161" y="0" width="11.5" height="11.7" fill="#777"/><rect x="172.5" y="0" width="11.5" height="11.7" fill="#666"/>
      <rect x="0" y="11.7" width="11.5" height="11.7" fill="#e33"/><rect x="11.5" y="11.7" width="11.5" height="11.7" fill="#ee5"/><rect x="23" y="11.7" width="11.5" height="11.7" fill="#3c6"/><rect x="34.5" y="11.7" width="11.5" height="11.7" fill="#3cc"/><rect x="46" y="11.7" width="11.5" height="11.7" fill="#36c"/><rect x="57.5" y="11.7" width="11.5" height="11.7" fill="#c3c"/><rect x="69" y="11.7" width="11.5" height="11.7" fill="#fafafa"/><rect x="80.5" y="11.7" width="11.5" height="11.7" fill="#e0e0e0"/><rect x="92" y="11.7" width="11.5" height="11.7" fill="#999"/><rect x="103.5" y="11.7" width="11.5" height="11.7" fill="#808080"/><rect x="115" y="11.7" width="11.5" height="11.7" fill="#666"/><rect x="126.5" y="11.7" width="11.5" height="11.7" fill="#555"/><rect x="138" y="11.7" width="11.5" height="11.7" fill="#444"/><rect x="149.5" y="11.7" width="11.5" height="11.7" fill="#222"/><rect x="161" y="11.7" width="11.5" height="11.7" fill="#111"/><rect x="172.5" y="11.7" width="11.5" height="11.7" fill="#000"/>
      <rect x="0" y="23.4" width="11.5" height="11.7" fill="#f99"/><rect x="11.5" y="23.4" width="11.5" height="11.7" fill="#fc9"/><rect x="23" y="23.4" width="11.5" height="11.7" fill="#ff9"/><rect x="34.5" y="23.4" width="11.5" height="11.7" fill="#cf9"/><rect x="46" y="23.4" width="11.5" height="11.7" fill="#9f9"/><rect x="57.5" y="23.4" width="11.5" height="11.7" fill="#9fc"/><rect x="69" y="23.4" width="11.5" height="11.7" fill="#9ff"/><rect x="80.5" y="23.4" width="11.5" height="11.7" fill="#9cf"/><rect x="92" y="23.4" width="11.5" height="11.7" fill="#99f"/><rect x="103.5" y="23.4" width="11.5" height="11.7" fill="#c9f"/><rect x="115" y="23.4" width="11.5" height="11.7" fill="#f9f"/><rect x="126.5" y="23.4" width="11.5" height="11.7" fill="#f9c"/><rect x="138" y="23.4" width="11.5" height="11.7" fill="#c99"/><rect x="149.5" y="23.4" width="11.5" height="11.7" fill="#c9c"/><rect x="161" y="23.4" width="11.5" height="11.7" fill="#99c"/><rect x="172.5" y="23.4" width="11.5" height="11.7" fill="#f88"/>
      <rect x="0" y="35.1" width="11.5" height="11.9" fill="#f66"/><rect x="11.5" y="35.1" width="11.5" height="11.9" fill="#f93"/><rect x="23" y="35.1" width="11.5" height="11.9" fill="#fe6"/><rect x="34.5" y="35.1" width="11.5" height="11.9" fill="#9e5"/><rect x="46" y="35.1" width="11.5" height="11.9" fill="#5d7"/><rect x="57.5" y="35.1" width="11.5" height="11.9" fill="#4db"/><rect x="69" y="35.1" width="11.5" height="11.9" fill="#3cf"/><rect x="80.5" y="35.1" width="11.5" height="11.9" fill="#39e"/><rect x="92" y="35.1" width="11.5" height="11.9" fill="#57d"/><rect x="103.5" y="35.1" width="11.5" height="11.9" fill="#75c"/><rect x="115" y="35.1" width="11.5" height="11.9" fill="#a5c"/><rect x="126.5" y="35.1" width="11.5" height="11.9" fill="#d5a"/><rect x="138" y="35.1" width="11.5" height="11.9" fill="#e57"/><rect x="149.5" y="35.1" width="11.5" height="11.9" fill="#c66"/><rect x="161" y="35.1" width="11.5" height="11.9" fill="#d48"/><rect x="172.5" y="35.1" width="11.5" height="11.9" fill="#f77"/>
    </g>
  </svg>
  <div class="abs btn-dark" style="left:704px;width:108px">SEARCH NOW <svg width="11" height="11"><circle cx="4.5" cy="4.5" r="3.3" fill="none" stroke="#fff" stroke-width="1.6"/><path d="M7 7l3 3" stroke="#fff" stroke-width="1.8"/></svg></div>
  <div class="abs btn-dark" style="left:819px;width:110px">RESET ALL <svg width="13" height="13" viewBox="0 0 13 13"><path d="M10.5 4A5 5 0 1 0 11 8" fill="none" stroke="#fff" stroke-width="1.6"/><path d="M8 1l3 3-3 1z" fill="#fff"/></svg></div>

  <aside class="abs sidebar">
    <h2>CATEGORIES</h2>
    <ul class="cat-list">
      <li>Agriculture</li><li>Animals &amp; Pets</li><li>Antique</li><li>App</li><li>Apparel</li><li>Architecture</li><li>Arts &amp; Culture</li><li>Art &amp; Photography</li><li>Auction Templates</li><li>Beauty</li><li>Blog</li><li>Books</li><li>Brewery</li><li>Business &amp; Employment</li><li>Cafe and Restaurant</li><li>Cars</li><li>Charity</li><li>Communications</li><li>Computers</li><li>Dating</li><li>Design</li><li>Education</li><li>Electronics</li><li>Entertainment</li><li>Environmental</li><li>Exterior design</li><li>Family</li><li>Fashion</li><li>Flowers</li><li>Food &amp; Drink</li><li>Games</li><li>General</li><li>Gifts</li><li>Health</li><li>Hobbies &amp; Crafts</li><li>Holiday Templates</li><li>Hosting</li><li>Hotels</li><li>Industrial</li><li class="more">+ more.....</li>
    </ul>
  </aside>

  <section class="abs hero">
    <h1>Lorem ipsum dolor sit amet</h1>
    <p>Excepteur sint occaecat cupidatat non proident</p>
    <span class="cta">VIEW MORE</span>
  </section>

  <section class="abs featured-site">
    <h3>FEATURED WEBSITE</h3>
    <div class="site-shot" role="img" aria-label="Screenshot of a black and white jewellery gallery website"></div>
  </section>

  <h2 class="abs section-title">FEATURED TEMPLATES</h2>
  <div class="abs pager"><i></i><span class="cur">1</span>|<span>2</span>|<span>3</span>|<span>4</span>|<span>5</span>|<span>6</span><i></i></div>

  <div class="abs tile" style="left:202px;top:604px"><div class="thumb" role="img" aria-label="Dental clinic website template preview" style="background:linear-gradient(#2b2f36 0 14%,#d9eef8 14% 55%,#f4f4f4 55% 92%,#333 92%)"></div><span class="add-btn">ADD TO CART</span><div class="tile-links">View Details &nbsp; | &nbsp;View Demo</div></div>
  <div class="abs tile" style="left:467px;top:604px"><div class="thumb" role="img" aria-label="Modern house at dusk with lit windows" style="background:linear-gradient(#3b3550,#6a5a6a 40%,#c08a4a 70%,#2a2228)"></div><span class="add-btn">ADD TO CART</span><div class="tile-links">View Details &nbsp; | &nbsp;View Demo</div></div>
  <div class="abs tile" style="left:732px;top:604px"><div class="thumb" role="img" aria-label="Construction company template with a modern house photo" style="background:linear-gradient(#1b2a55 0 8%,#2f5fa8 8%,#6a8fc8 50%,#c7883a 75%,#2a2a2a)"></div><span class="add-btn">ADD TO CART</span><div class="tile-links">View Details &nbsp; | &nbsp;View Demo</div></div>
  <div class="abs tile" style="left:202px;top:863px"><div class="thumb" role="img" aria-label="Abstract orange and yellow light streaks" style="background:linear-gradient(135deg,#c85a00,#f6a400 45%,#ffd24a 55%,#d86a00)"></div><span class="add-btn">ADD TO CART</span><div class="tile-links">View Details &nbsp; | &nbsp;View Demo</div></div>
  <div class="abs tile" style="left:467px;top:863px"><div class="thumb" role="img" aria-label="Diamond ring on a purple background" style="background:radial-gradient(circle at 50% 50%,#e8e8ea,#8b8a95 30%,#4a2b55 60%,#1d1420)"></div><span class="add-btn">ADD TO CART</span><div class="tile-links">View Details &nbsp; | &nbsp;View Demo</div></div>
  <div class="abs tile" style="left:732px;top:863px"><div class="thumb" role="img" aria-label="Blue vertical light curtain background" style="background:linear-gradient(90deg,#061d4a,#0f4c9a 35%,#3fb4ee 55%,#0f4c9a 75%,#061d4a)"></div><span class="add-btn">ADD TO CART</span><div class="tile-links">View Details &nbsp; | &nbsp;View Demo</div></div>

  <footer class="abs footer">
    <nav>Home<span>|</span>About Us<span>|</span>Templates<span>|</span>Sitemap<span>|</span>Contact Us<span>|</span>Help &amp; Support<span>|</span>Affiliate Program<span>|</span>Privacy Policy<span>|</span>Terms &amp; Conditions</nav>
    <div class="copy">© 2013 Kelvora.</div>
  </footer>
</div>
</body>
</html>
```